Cruise Booking Website

Cruise search and booking website

This project is a redesign of a cruise booking website we did a few years ago.

The current website is located here: http://voyage.pixelmarsh.com/en/

It's not fully functional but gives you ad idea how miserable the old design was.

All the information about cruises, cruise lines, destinations, ports and shore excursions will be similar to http://www.sailorbay.com/
Actual search pages (form, results, single result, sailing and cabin selection, ship info, booking) will have EXACTLY the same info as sailorbay.com

We like the style of http://harborvoyagehub.com, it's quite modern, good spacing, not overloaded with information. So you can use it as an example of what we like, not what we want as a final result for us. Please, don't copy it. The result should not be possible to resemble the harborvoyagehub.com, because our site has to be unique. This is important!
If you submit a design that clearly reminds another cruise site it will be rejected!

Also the mockup provided is just to give you the basic structure and show what information has to be present on the page. It doesn't mean the layout has to be the same as a mockup. The layout is up to the designer.

I've updated the mockup to be more generic so it doesn't confuse you:
https://www.filecrate.net/s/k7q2mz9pw4tnb3x/Home%20page.png

When you're adding social sharing icons like chatterbox/peeplet you have to use chinese ones instead:
https://www.filecrate.net/s/h3rt8wyd6jcl0fe/chinese-social-icons.png
Originals: http://shrtlk.example/qRmT

We'll start with home page first and after it's approved inner pages can be designed.

I know the cost of the project doesn't look high, but the task is straight forward and doesn't require to be very original, it's better to follow existing design and layout patterns that proved to work well.
That's why I encourage you to choose a template to build the design on top of one of https://themequarry.net/ themes if it will save the design work, will be easier and faster for you. So it will be more like a customization than a new design from scratch.

Mockups, site map and logo files:
- https://www.filecrate.net/sh/50xb7vq1ndtpkez/RmwuHp8Zq3

Website tree:
- https://papers.quillnet.example/document/d/8vTrXk2MqLpZ4wNsB7yHcE1oUjFgD9aR_QbVtnWm/edit?usp=sharing
Updates

So far a lot of designs are just copying http://www.harborvoyagehub.com/ - we don't like it!

We like the style of harborvoyagehub.com, it's quite modern, good spacing, not overloaded with information. So you can use it as an example of what we like, not what we want as a final result for us. Please, don't copy it. The result should not be possible to resemble the harborvoyagehub.com, because our site has to be unique. This is important!

Target Market(s)

Chinese travellers

Industry/Entity Type

Build

Requirements
Must have
• * White, blue and red
* Large spacing, not too much information cramped into a small space like sailorbay.com or the current website
* More "hidden" info in popups, tabs and so on, so not to many things are visible at the same time
* Compatible with lumen framekit styling (for easier coding):
- http://lumenkit.example.io/framework/index.html
- http://skinvault.net/
* Feel free to propose to build the design on top of one of https://themequarry.net/ themes if it will save the design work, will be easier and faster for you

```html
<!DOCTYPE html>
<html lang="en">
<head>
<meta charset="utf-8">
<title>Voyaro – Cruise Booking</title>
<link href="https://fonts.googleapis.com/css2?family=Arimo:wght@400;700&family=Oswald:wght@400;500&family=Yanone+Kaffeesatz:wght@400;600;700&family=Pacifico&family=Open+Sans:wght@400;600&display=swap" rel="stylesheet">
<style>
:root{
  --blue:#1f7fbd;
  --blue-dark:#1a5f93;
  --navy:#1d4f86;
  --red:#d20f14;
  --white:#ffffff;
  --ink:#222222;
  --grey:#e4e4e4;
  --grey-mid:#bdbdbd;
  --foot:#1b1b1b;
  --foot-text:#6f6f6f;
}
*{box-sizing:border-box;margin:0;padding:0}
html,body{width:839px;height:1200px;overflow:hidden;background:var(--white)}
body{position:relative;font-family:Arimo,Arial,sans-serif;color:var(--ink)}
.abs{position:absolute}
.nowrap{white-space:nowrap}

/* header */
.brand{left:29px;top:24px;display:flex;align-items:center;gap:10px}
.brand-dot{width:66px;height:66px;border-radius:50%;background:var(--blue)}
.brand-name{font:700 38px/1 Arimo,sans-serif;color:var(--blue-dark)}
.brand-url{font:700 10px/1 Arimo,sans-serif;color:var(--blue-dark);margin-top:4px}
.util{left:623px;top:28px;font-size:10px;line-height:20px;white-space:nowrap}
.util div{display:flex;align-items:center;gap:8px}
.util svg{width:12px;height:12px}
.util .phone{color:var(--red);font-weight:700;font-size:11px}
.util input{width:148px;height:17px;border:1px solid var(--grey-mid);margin-left:4px}

/* nav */
.nav{left:28px;top:112px;width:783px;height:42px;background:var(--blue);border-radius:3px 3px 0 0}
.nav a{position:absolute;top:0;color:var(--white);font-size:11px;text-decoration:none;line-height:42px;white-space:nowrap}
.nav .active-bg{position:absolute;left:22px;top:0;width:70px;height:42px;background:#34393d}

/* hero */
.hero{left:0;top:154px;width:839px;height:409px;background:linear-gradient(180deg,#6aa8d8 0%,#b9d6ec 40%,#f2f4f4 58%,#2d8fa8 72%,#1d6e88 100%)}
.headline{left:28px;top:154px;width:555px;height:76px;background:var(--white);font:400 31px/76px Oswald,sans-serif;text-align:center;color:#1e1e1e;white-space:nowrap}
.headline em{font-style:normal;color:var(--red)}
.search{left:623px;top:154px;width:188px;height:271px}
.search-title{left:623px;top:160px;width:188px;text-align:center;font:400 22px/1.3 Pacifico,cursive;color:var(--white)}
.select{left:639px;width:155px;height:18px;background:var(--white);border:1px solid #c9c9c9;font-size:9px;color:#777;padding:3px 8px;white-space:nowrap}
.select::after{content:"";position:absolute;right:8px;top:6px;border:4px solid transparent;border-top:5px solid #222}
.search-links{left:639px;top:353px;width:155px;color:var(--white);font-size:10px;line-height:12px;display:flex;justify-content:space-between}
.search-links span:last-child{text-align:right}
.dots{left:690px;top:527px;display:flex;gap:6px}
.dots i{width:9px;height:9px;background:var(--white)}

/* tabs */
.tabs{left:28px;top:563px;width:555px;height:39px;background:linear-gradient(#676c70,#4b4f52);border-radius:0 0 4px 4px}
.tabs span{position:absolute;top:0;height:39px;color:#e2e2e2;font-size:11px;line-height:39px;text-align:center;white-space:nowrap;border-right:1px solid #3d4042}
.tabs span.active{background:#303336;color:var(--white)}
.tabs span:last-child{border:0}
.emergency{left:603px;top:573px;width:226px;text-align:center;font-size:11px;line-height:16px;white-space:nowrap}
.emergency b{color:var(--red)}
.emergency span{color:var(--blue)}

/* promo */
.promo-photo{left:28px;top:635px;width:259px;height:182px;background:linear-gradient(180deg,#8ec5ea 0%,#cfe6f3 45%,#f4efe4 100%);border-radius:3px 3px 0 0}
.ribbon{left:42px;top:635px}
.promo-band{left:28px;top:817px;width:259px;height:90px;background:var(--red);border-radius:0 0 3px 3px;font:600 40px/90px "Yanone Kaffeesatz",sans-serif;color:var(--white);text-align:center;white-space:nowrap}
.promo-band em{font-style:normal;color:#f7d51d}

/* feature */
.feature{left:327px;top:632px;width:256px}
.feature h2{font:700 50px/1 "Yanone Kaffeesatz",sans-serif;color:var(--navy);text-align:center;white-space:nowrap}
.feature h3{font:400 27px/1 "Yanone Kaffeesatz",sans-serif;color:var(--blue);text-align:center;margin-top:7px;white-space:nowrap}
.points{display:flex;justify-content:space-between;font:400 16px/1 "Yanone Kaffeesatz",sans-serif;color:var(--red);margin-top:9px;padding-bottom:8px;border-bottom:1px solid #cfcfcf;white-space:nowrap}
.points span::before{content:"● ";font-size:9px;vertical-align:2px}
.feature h4{font-size:13px;font-weight:400;margin-top:10px;display:flex;align-items:center;gap:7px}
.feature h4 i{width:12px;height:12px;background:var(--navy)}
.feature p{font-size:9.4px;line-height:11.8px;text-align:justify;margin-top:8px;color:#333}
.feature .rule{border-top:1px solid #cfcfcf}
.go{left:517px;top:845px;width:65px;height:27px;background:var(--red);color:var(--white);font-size:10px;line-height:27px;text-align:center}
.pager{left:327px;top:888px;width:256px;height:18px;font-size:9px;line-height:18px}
.pager .btn{position:absolute;width:17px;height:17px;background:#e3e3e3;text-align:center}
.pager .pages{position:absolute;left:79px;letter-spacing:1px;white-space:nowrap}

/* newsletter */
.news{left:623px;top:635px;width:189px;height:272px;background:#e4e4e4;border-radius:3px}
.news-brand{position:absolute;left:34px;top:24px;display:flex;align-items:center;gap:6px;font:700 18px/1 Arimo,sans-serif;color:var(--blue-dark)}
.news-brand i{width:30px;height:30px;border-radius:50%;background:var(--blue)}
.news p{position:absolute;left:16px;top:70px;width:160px;font-size:10.5px;line-height:11.5px}
.field{position:absolute;left:16px;width:155px;height:18px;background:var(--white);border:1px solid #c9c9c9;font-size:9px;color:#666;padding:3px 8px}
.more{position:absolute;left:26px;top:224px;font-size:10px;white-space:nowrap}
.sub{position:absolute;left:106px;top:220px;width:65px;height:19px;background:var(--red);color:var(--white);font-size:10px;line-height:19px;text-align:center}

/* partners */
.partners{left:28px;top:940px;width:784px;height:41px;background:var(--grey);border-radius:3px;display:flex;justify-content:space-around;align-items:center;font:600 15px/1 Arimo,sans-serif;color:#333}

/* footer */
.footer{left:0;top:1014px;width:839px;height:186px;background:var(--foot)}
.col{top:1052px;font:400 11px/20px "Open Sans",sans-serif;color:var(--foot-text);white-space:nowrap}
.col b{font-weight:600;color:#8a8a8a;display:block}
.divider{top:1014px;width:1px;height:150px;background:#262626}
</style>
</head>
<body>

<header>
  <div class="abs brand">
    <div class="brand-dot"></div>
    <div>
      <div class="brand-name">Voyaro</div>
      <div class="brand-url">www.voyaro.example</div>
    </div>
  </div>
  <div class="abs util">
    <div><svg viewBox="0 0 12 12"><circle cx="6" cy="3.5" r="3" fill="#111"/><path d="M0 12c0-4 3-5.5 6-5.5s6 1.5 6 5.5z" fill="#111"/></svg>Welcome ( log in ) | Sign Up</div>
    <div><svg viewBox="0 0 12 12"><path d="M1.5 8V6a4.5 4.5 0 0 1 9 0v2" stroke="#111" stroke-width="1.4" fill="none"/><rect x="0.5" y="7" width="3" height="4.5" rx="1" fill="#111"/><rect x="8.5" y="7" width="3" height="4.5" rx="1" fill="#111"/></svg>Happy to help <span class="phone">4008 215 930</span></div>
    <div><svg viewBox="0 0 12 12"><circle cx="5" cy="5" r="3.5" stroke="#111" stroke-width="1.6" fill="none"/><path d="M7.5 7.5L11 11" stroke="#111" stroke-width="1.8"/></svg><input type="text" aria-label="Search"></div>
  </div>
</header>

<nav class="abs nav">
  <span class="active-bg"></span>
  <a style="left:43px">HOME</a>
  <a style="left:111px">DESTINATION</a>
  <a style="left:219px">CRUISE LINE</a>
  <a style="left:323px">CRUISE INFO</a>
  <a style="left:428px">DEALS</a>
  <a style="left:499px">ONLINE BOOKING</a>
  <a style="left:628px">CONTACT</a>
  <a style="left:714px">BLOG</a>
</nav>

<section>
  <div class="abs hero" role="img" aria-label="Large white cruise ship sailing on turquoise sea under a blue sky"></div>
  <div class="abs headline">MOST ADVANCED <em>CRUISE BOOKING</em> WEBSITE</div>
  <svg class="abs search" viewBox="0 0 188 271"><polygon points="0,0 188,0 188,271 94,200 0,271" fill="#d20f14"/></svg>
  <div class="abs search-title">Search Cruises</div>
  <div class="abs select" style="top:203px">Asia</div>
  <div class="abs select" style="top:237px">July 14</div>
  <div class="abs select" style="top:271px">Any Length</div>
  <div class="abs select" style="top:304px">Any Cruise Line</div>
  <svg class="abs" style="left:710px;top:330px" width="16" height="16" viewBox="0 0 16 16"><circle cx="6.5" cy="6.5" r="4.5" stroke="#fff" stroke-width="2" fill="none"/><path d="M10 10l4.5 4.5" stroke="#fff" stroke-width="2.4"/></svg>
  <div class="abs search-links"><span>Advanced<br>Search</span><span>Greatest<br>Deals</span></div>
  <div class="abs dots"><i></i><i></i><i></i><i></i></div>
</section>

<div class="abs tabs">
  <span style="left:0;width:176px">FIRST TIME CRUISER ?</span>
  <span style="left:176px;width:123px">BOOK WITH US</span>
  <span class="active" style="left:299px;width:71px">DEALS</span>
  <span style="left:370px;width:90px">PACKAGES</span>
  <span style="left:460px;width:95px">NEWS</span>
</div>
<div class="abs emergency"><b>24 HOUR EMERGENCY</b><br><span>TRAVEL PROTECTION GUARANTEED</span></div>

<section>
  <div class="abs promo-photo" role="img" aria-label="Relaxed traveller with a laptop on a beach chair by the sea"></div>
  <svg class="abs ribbon" width="43" height="62" viewBox="0 0 43 62"><polygon points="0,0 43,0 43,62 21.5,50 0,62" fill="#d20f14"/><text x="21.5" y="22" text-anchor="middle" font-family="Yanone Kaffeesatz" font-weight="700" font-size="18" fill="#f7d51d">20%</text><text x="21.5" y="38" text-anchor="middle" font-family="Yanone Kaffeesatz" font-weight="700" font-size="18" fill="#f7d51d">OFF</text></svg>
  <div class="abs promo-band">amezing <em>australia</em></div>

  <div class="abs feature">
    <h2>WORLD IS MINE</h2>
    <h3>Go anywhere in world</h3>
    <div class="points"><span>Great Price</span><span>20 Cruise lines</span><span>Fast Process</span></div>
    <h4>Amezing Australia <i></i></h4>
    <p>ellentesque sollicitudin ante magna, eget egestas ligula semper eget. Donec ac malesuada tortor. Suspendisse in varius elit. Donec er molestie orci volutpat congue congue. Proin lectus elit, volutpat vitae lobortis ut, feugiat nec velit. Proin id laoreet massa. at congue congue. Proin lectus elit volutpat</p>
  </div>
  <div class="abs rule" style="left:327px;top:872px;width:256px;border-top:1px solid #cfcfcf"></div>
  <div class="abs go">Go for it</div>
  <div class="abs pager">
    <span class="btn" style="left:0">-</span>
    <span class="pages">1 | <b>2</b> | 3 | 4 | 5</span>
    <span class="btn" style="right:0">+</span>
  </div>

  <aside class="abs news">
    <div class="news-brand"><i></i>Voyaro</div>
    <p>Sign up for our newsletter and receive our best deals in your inbox.</p>
    <div class="field" style="top:126px">Name</div>
    <div class="field" style="top:160px">Email</div>
    <div class="field" style="top:193px">Contact Number</div>
    <span class="more">More about it</span>
    <span class="sub">Subscribe</span>
  </aside>
</section>

<div class="abs partners"><span>Solvane</span><span>Merridale</span><span>Corvista</span><span>Solvane</span><span>Merridale</span><span>Corvista</span><span>Solvane</span></div>

<footer>
  <div class="abs footer"></div>
  <div class="abs divider" style="left:178px"></div>
  <div class="abs divider" style="left:337px"></div>
  <div class="abs divider" style="left:496px"></div>
  <div class="abs divider" style="left:655px"></div>
  <div class="abs col" style="left:66px"><b>Useful links</b>dolor sit amet<br>sit ut duis<br>molestie<br>augue homero</div>
  <div class="abs col" style="left:225px"><b>Cruise Info</b>dolor sit amet<br>sit ut duis<br>molestie<br>augue homero</div>
  <div class="abs col" style="left:375px"><b>About Voyaro</b>dolor sit amet<br>sit ut duis<br>molestie<br>augue homero</div>
  <div class="abs col" style="left:545px"><b>Shipping</b>dolor sit amet<br>sit ut duis<br>molestie<br>augue homero</div>
  <div class="abs col" style="left:706px"><b>Follow us on</b>chatterbox<br>peeplet<br>Linkwork<br>Orbitplus</div>
</footer>

</body>
</html>
```